Blind dating / hook up web

We're creating a new web application based on blind dates to hook up with others who like you (occasional dating, not long-term relationships): www.velvetquorra.com
The background idea is the same as other dating websites (there're many differences but probably don't matter for the design): to browse potential matching profiles based on several criteria (age, gender, zone, etc.) and vote for the ones you like (a yes/no answer just seeing the pictures and basic info, option to see the detailed profile including other users feedback about that profile). The other users do the same, and then, you can see the real matches and contact them.
The one who start the contact to matched profiles, should pay for it, discounting the cost from a previously funded credit balance.
There's also a section to browse for meeting places/plans suggestions.
After you had any date, you could leave feedback about the other, so, everyone had a reputation (similar to the tradlo's feedback system).
Of course, the other typical options: register/mail verification, profile edit, "loading..." stuff, etc.
We'll start with a typical website application, but we'll move to mobile app soon, so, a responsive design will be a plus.

We expect to get a design to use as a pattern to develop (our job) the application, so, we'll need to work with the winning designer to get the graphical pieces/elements (backgrounds, icons, sprites, etc.) not only the whole screen captures. We'll contact the finalists to discuss details about how much of this are included or not and possible future work if we need it.

We've got no previous work done on logos or color schemes, so, feel free to work on whatever you want.

Please, feel free to ask for details if you need more: plinthworksltd@maremail.example

One preference on our web development will be to use Scaffoldr (or similar frameworks), so, if you know about it and you'd like to take in care, this will be a plus, not a must. If you think there will be something to gain on other design patterns, please, forget Scaffoldr and put preference on the design itself.

After received the first drafts, I think there's something general to clarify:

Everybody seem to tend to include several romantic references... the website will not be dedicated to find a long term relationship but occasional affairs, so, maybe hearts aren't the best symbol and romantic pictures/slogans the best resources. 
Also we're searching for a different design/concept than other dating services... there're some key points to make it special (different from typical date websites): 
- Mark potential matching profiles with answering a simply Yes/No (I like / I don't like) 
- Blind dates: you finally don't know who are you going to meet, you just know both answered Yes. So, intrigue will be a better idea than love. 

Let’sfocus a little more what we have in mind to be a different dating site andwhat we expect to obtain with this design project:

The mainfunctionalities and, so, the most important parts to design are:

1. Viewinga sequence of potential matching profiles, answer a question similar to “do youwant to hook up he/she/them?” Clearly more “hot” than “sweet”… more erotic (notX) than love/tender… more prohibited/hidden/secret thanstandard/traditional/public/familiar…

This simplysystem can be the principal idea so, could take a good place in the home,before register showing the best rated profiles, and after register to show thepotential matches.

The sitewon’t be restricted to men/women, it will allow to register as couple too andthe mix of sexual orientations hetero/bi/homo... Of course you should registerand choose your filter parameters, but you’ll do it sometimes, not in everyvisit to the site.

The usershould see a big picture of each profile (this is the first attraction, we’rehooking up not searching for our whole-life partner) and just a few otherdetails like age and feedback rating from other users that already met thatprofile.

Thereshould be a way to review what profiles did you answer Yes and what No.

2. Anotherimportant part of the site is the one to create and propose meet plans. You canpost here your fantasies, your plans, your suggestions about what do you wantto do or what you propose for the meeting. This is where the search engine willtake place, to propose you places, ideas or services based on what you’refinding. This will be some kind of wizard or assistant, to “configure” yourideal meeting. It should suggest you activities to include in your plan and thesearch engine will suggest related places related to that activities. I.e.: ifI’d like to take a dinner, grab some beers and finish the night on a 5 starhotel suite, I’ll add “Dinner ideas”, “going out ideas” and “night stay ideas”(or something similar) and the engine will suggest me some near restaurants,pubs and hotels. Of course, you can enter your personalized plan manually inplain text or just select activities without taking any suggestion. (reserve aplace to suggest new activities to the system!)

Afterconfiguring your plan, you can post it to be realized some days and expose itto your matches to find anyone that like your plan.

This wizardwill allow you to browse the past plans to edit/reuse them and also receiveanswers from the matching profiles who like your plant to initiate the finalcontact and meet them.

3. Inanother section you should see plans posted by others and have the way toaccept or discard them.

4. Ofcourse, the homepage must not be as simple as the Yes/No answering section, it’simportant to explain what the service are and how it works, but, for us, it’smore important to see how the “daily” operative will show up than the home,because the home must be a reflect, a summary, of the operative surrounded bycatching slogans.

There’realso several related or secondary screens and resources to be designed, but,first, we’ll to focus on these four things. Drafts should reflect these ideasor will be very difficult to fit.

After revising a lot of designs sent, there's something we're doing wrong... maybe I'm not explaining myself well, so, let me try again to expose some important ideas and add some others that had appeared after a few designs that I thing they're on the right way:

- the site should be different from the "standard" dating services. Think more in casual meetings, sex encounters, swingers, hot nights, etc. Men, women or couples (even groups!) looking for anything... so, think on any kind of sexual orientation. People live in a stressed society, they're finding something different without loosing time... something spicy, intrigue, surprise, horny... just fun, not love, no sweet, no false promises... but at the same time, think on another way to structure it, another point of view, not the typical Register, browse, contact, meet.
- please, avoid the "register" form directly on the home... the user should take a full free tour all over the site without registering. The site will collect information about his/her/their preferences while he/she/they are looking what the site is about. When clicking on something that really need to be registered, then, the register form will appear already filled with all the collected information. Some kind of remember should appear if the user is using the site for a long time stuck, for example, answering yes/no to the profiles. But there shouldn't be any pressure to register, it should be a natural need after a while.
- The landing homepage should accomplish just three main objectives:
1. Explain what the service are about in just a few sentences (more about it later)
2. Choose your profile type preferences (I'm looking for...): men/women/couples, taking in care that I could find one, two or all three options... and enter to the site to see profiles
3. If I'm already registered, log in.
The login should be easy to see and find, but shouldn't be take too much importance.
The explaining sentences/section should be also easy to see, but can be a scroll down section
The most important and eye-catching should be the selector... with naughty pictures of men/women/couples to mark what you're looking for... maybe a title "What are you looking for?" and a site entrance "Let's hook-up!" that appears after choosing at least one option...
- After the landing homepage, the operational sections described on the previous update... where the backgrounds (and maybe the whole theme) should change according the user preferences... (don't show a women picture if the user isn't looking for women).
Don't think about if the design will end in a very difficult development! it's more important to have a good design and then, our developers will find the way to implement it. Don't be afraid of it! let your talent flow freely ;)

Many of your are using some kind of form to enter the search parameters... We want to try to avoid this and we're thinking on integrate the form on the homepage itself... something like to use icons to select "what I'm" (Man/Woman/Couple... in a similar way as many of you are showing the total profiles of each...); then, a second, bigger, selector to choose "what I'm looking for" (Men/Women/Couples, could select one or many)... maybe playing with big pictures or the background itself; finally (perhaps integrated with the results) some kind of slider to select the age range, leaving only the dropdowns to select the geographic location (if no one has a better idea with no typical "fields").

Reason: Some of you are in a very good way, but probably you need some more time to make your ideas shine ;)

```html
<!DOCTYPE html>
<html lang="en">
<head>
<meta charset="utf-8">
<title>Velvetquorra – Blind Dates</title>
<link rel="stylesheet" href="https://fonts.googleapis.com/css2?family=Ubuntu:wght@400;500&family=Open+Sans:wght@400;600&display=swap">
<style>
:root{
  --maroon:#720a0d;
  --red:#a80f12;
  --band-red:#ad0e12;
  --bright-red:#e0131a;
  --line-red:#e5141b;
  --blue:#13a2e0;
  --blue-dark:#0c6e9c;
  --teal:#1aa6d8;
  --field:#7b0b0e;
  --page:#f6f6f6;
  --ink:#555;
  --footer:#252525;
  --footer-bottom:#111;
  --white:#fff;
}
*{box-sizing:border-box;margin:0;padding:0}
html,body{width:1102px;height:1200px;overflow:hidden}
body{position:relative;font-family:"Open Sans",sans-serif;background:var(--page);color:var(--ink)}
.abs{position:absolute}

/* header */
.site-header{left:0;top:0;width:1102px;height:70px;background:var(--maroon);border-bottom:3px solid var(--line-red)}
.brand{left:118px;top:18px;font-family:"Ubuntu",sans-serif;font-weight:500;font-size:27px;color:var(--white);letter-spacing:.3px}
.login-btn{left:819px;top:24px;width:111px;height:27px;background:#5e0709;border-radius:2px;color:var(--white);font-size:10.5px;display:flex;align-items:center;padding-left:12px;gap:7px}
.login-btn .dot{width:13px;height:13px;border-radius:50%;background:#1f7fc0;display:flex;align-items:center;justify-content:center}
.lang-btn{left:937px;top:24px;width:47px;height:27px;background:#5e0709;border-radius:2px;display:flex;align-items:center;justify-content:center;gap:4px}
.flag{width:11px;height:8px;background:linear-gradient(#c33 0 50%,#fff 50%);position:relative}
.flag::before{content:"";position:absolute;left:0;top:0;width:5px;height:4px;background:#2a4fa0}
.caret{width:0;height:0;border-left:3.5px solid transparent;border-right:3.5px solid transparent;border-top:4px solid var(--white)}

/* hero */
.hero-photo{left:0;top:73px;width:1102px;height:520px;background:radial-gradient(ellipse at 35% 55%,#a7835a 0%,#6d4e34 45%,#2e211a 100%)}
.join-panel{left:638px;top:94px;width:346px;height:480px;background:var(--red)}
.join-title{left:0;top:22px;width:346px;text-align:center;font-family:"Ubuntu",sans-serif;font-size:24px;color:var(--white)}
.join-rule{left:52px;top:61px;width:244px;height:1px;background:rgba(255,255,255,.2)}
.pick-row{left:51px;top:76px;width:250px;height:24px;color:var(--white);font-size:9.5px;font-weight:600}
.field{left:52px;width:243px;height:40px;background:var(--field);color:var(--white);font-size:12.5px;display:flex;align-items:center;padding-left:14px}
.field.select{justify-content:space-between;padding-right:10px}
.join-btn{left:-14px;top:377px;width:374px;height:50px;background:var(--blue);color:var(--white);font-family:"Ubuntu",sans-serif;font-size:22px;display:flex;align-items:center;justify-content:center}
.fold{top:427px;width:0;height:0}
.fold.l{left:-14px;border-top:8px solid var(--blue-dark);border-left:14px solid transparent}
.fold.r{left:346px;border-top:8px solid var(--blue-dark);border-right:14px solid transparent}
.terms{left:0;top:441px;width:346px;text-align:center;color:var(--white);font-size:10.5px;line-height:12px}

/* blind dates */
.section-title{left:0;top:628px;width:1102px;text-align:center;font-family:"Ubuntu",sans-serif;font-size:29px;color:var(--bright-red)}
.section-intro{left:120px;top:674px;width:862px;text-align:center;font-size:13.5px;line-height:16px;color:var(--ink)}
.profile{top:730px;width:110px;text-align:center}
.avatar{width:80px;height:80px;border-radius:50%;margin:0 auto;background:radial-gradient(circle at 50% 40%,#d7b08f,#6b4a37)}
.p-name{margin-top:8px;font-size:15px;color:#666;line-height:18px}
.p-meta{margin-top:3px;font-size:9.8px;line-height:12px;color:#555}
.btn-like,.btn-unlike{width:67px;height:21px;margin:0 auto;border-radius:2px;color:var(--white);font-size:11px;display:flex;align-items:center;justify-content:center;gap:5px}
.btn-like{margin-top:9px;background:var(--bright-red)}
.btn-unlike{margin-top:6px;background:var(--teal)}

/* feedback */
.feedback-band{left:0;top:965px;width:1102px;height:92px;background:var(--band-red)}
.feedback-label{left:118px;top:32px;font-family:"Ubuntu",sans-serif;font-size:22px;color:var(--white)}
.feedback-input{left:537px;top:27px;width:239px;height:38px;background:var(--white);border-radius:2px;font-size:12px;color:#aaa;display:flex;align-items:center;padding-left:21px}
.feedback-submit{left:786px;top:27px;width:198px;height:38px;background:var(--maroon);border-radius:2px;color:var(--white);font-family:"Ubuntu",sans-serif;font-size:17px;display:flex;align-items:center;justify-content:center}

/* footer */
.site-footer{left:0;top:1057px;width:1102px;height:109px;background:var(--footer);color:var(--white)}
.foot-head{font-family:"Ubuntu",sans-serif;font-size:15px}
.foot-rule{height:1px;background:#555}
.quick-links{left:118px;top:75px;font-size:11px;word-spacing:1px}
.quick-links span{margin:0 7px}
.social{top:73px;width:19px;height:19px;border-radius:50%;background:var(--white)}
.copyright-bar{left:0;top:1166px;width:1102px;height:34px;background:var(--footer-bottom);color:var(--white);font-size:10px;padding:10px 0 0 119px}
</style>
</head>
<body>

<header class="site-header abs">
  <div class="brand abs">Velvetquorra</div>
  <div class="login-btn abs"><span class="dot"><span class="caret" style="transform:rotate(90deg);border-top-width:3px"></span></span>Member Login</div>
  <div class="lang-btn abs"><span class="flag"></span><span class="caret"></span></div>
</header>

<div class="hero-photo abs" role="img" aria-label="Photo of a couple on a dinner date at a candlelit table"></div>

<section class="join-panel abs">
  <h2 class="join-title abs" style="font-weight:400">Join us</h2>
  <div class="join-rule abs"></div>
  <div class="pick-row abs">
    <svg width="250" height="24" viewBox="0 0 250 24">
      <text x="0" y="15" fill="#fff" font-family="Open Sans, sans-serif" font-size="9.5" font-weight="600">I am</text>
      <circle cx="34" cy="12" r="4" fill="#fff"/><circle cx="34" cy="12" r="1.6" fill="#7b0b0e"/>
      <g fill="#fff"><circle cx="47" cy="3.5" r="2.2"/><rect x="44.5" y="6.5" width="5" height="8" rx="1"/><rect x="45" y="14" width="1.7" height="7"/><rect x="47.3" y="14" width="1.7" height="7"/></g>
      <circle cx="69" cy="12" r="4" fill="#7b0b0e"/>
      <g fill="#fff"><circle cx="82" cy="3.5" r="2.2"/><path d="M79.5 6.5h5l2 9h-9z"/><rect x="80" y="15" width="1.7" height="6"/><rect x="82.3" y="15" width="1.7" height="6"/></g>
      <text x="140" y="15" fill="#fff" font-family="Open Sans, sans-serif" font-size="9.5" font-weight="600">Looking for</text>
      <rect x="196" y="7" width="10" height="10" fill="#7b0b0e"/>
      <g fill="#fff"><circle cx="213" cy="3.5" r="2.2"/><rect x="210.5" y="6.5" width="5" height="8" rx="1"/><rect x="211" y="14" width="1.7" height="7"/><rect x="213.3" y="14" width="1.7" height="7"/></g>
      <rect x="228" y="7" width="10" height="10" fill="#7b0b0e"/>
      <g fill="#fff"><circle cx="245" cy="3.5" r="2.2"/><path d="M242.5 6.5h5l2 9h-9z"/><rect x="243" y="15" width="1.7" height="6"/><rect x="245.3" y="15" width="1.7" height="6"/></g>
    </svg>
  </div>
  <div class="field abs" style="top:107px">Name</div>
  <div class="field select abs" style="top:159px;width:116px">Month <span class="caret"></span></div>
  <div class="field select abs" style="top:159px;left:176px;width:56px;padding-left:10px">Day <span class="caret"></span></div>
  <div class="field select abs" style="top:159px;left:239px;width:56px;padding-left:8px">Year <span class="caret"></span></div>
  <div class="field select abs" style="top:211px">Country <span class="caret"></span></div>
  <div class="field abs" style="top:264px">Enter your username</div>
  <div class="field abs" style="top:316px">Enter your Password</div>
  <div class="join-btn abs">Join Now!</div>
  <div class="fold l abs"></div>
  <div class="fold r abs"></div>
  <p class="terms abs">By clicking this button you are agreeing to our<br>Terms &amp; Conditions</p>
</section>

<h2 class="section-title abs" style="font-weight:400">Blind Dates</h2>
<p class="section-intro abs">You can register and create your profile for FREE! you finally don't know who are you going to meet, you just know both answered Yes. So, intrigue will be a better idea than love.</p>

<div class="profile abs" style="left:103px"><div class="avatar" role="img" aria-label="Member profile photo"></div><div class="p-name">Anthony</div><div class="p-meta">Registered 1 hours,<br>20 minutes ago</div><div class="btn-like">&#9829; Like</div><div class="btn-unlike">&#9825; UnLike</div></div>
<div class="profile abs" style="left:215px"><div class="avatar" role="img" aria-label="Member profile photo"></div><div class="p-name">packys</div><div class="p-meta">Registered 1 day,<br>12hours ago</div><div class="btn-like">&#9829; Like</div><div class="btn-unlike">&#9825; UnLike</div></div>
<div class="profile abs" style="left:329px"><div class="avatar" role="img" aria-label="Member profile photo"></div><div class="p-name">Anthony</div><div class="p-meta">Registered 1 hours,<br>20 minutes ago</div><div class="btn-like">&#9829; Like</div><div class="btn-unlike">&#9825; UnLike</div></div>
<div class="profile abs" style="left:441px"><div class="avatar" role="img" aria-label="Member profile photo"></div><div class="p-name">packys</div><div class="p-meta">Registered 1 day,<br>12hours ago</div><div class="btn-like">&#9829; Like</div><div class="btn-unlike">&#9825; UnLike</div></div>
<div class="profile abs" style="left:553px"><div class="avatar" role="img" aria-label="Member profile photo"></div><div class="p-name">Anthony</div><div class="p-meta">Registered 1 hours,<br>20 minutes ago</div><div class="btn-like">&#9829; Like</div><div class="btn-unlike">&#9825; UnLike</div></div>
<div class="profile abs" style="left:665px"><div class="avatar" role="img" aria-label="Member profile photo"></div><div class="p-name">packys</div><div class="p-meta">Registered 1 day,<br>12hours ago</div><div class="btn-like">&#9829; Like</div><div class="btn-unlike">&#9825; UnLike</div></div>
<div class="profile abs" style="left:777px"><div class="avatar" role="img" aria-label="Member profile photo"></div><div class="p-name">Anthony</div><div class="p-meta">Registered 1 hours,<br>20 minutes ago</div><div class="btn-like">&#9829; Like</div><div class="btn-unlike">&#9825; UnLike</div></div>
<div class="profile abs" style="left:890px"><div class="avatar" role="img" aria-label="Member profile photo"></div><div class="p-name">packys</div><div class="p-meta">Registered 1 day,<br>12hours ago</div><div class="btn-like">&#9829; Like</div><div class="btn-unlike">&#9825; UnLike</div></div>

<section class="feedback-band abs">
  <p class="feedback-label abs">you could leave feedback about the other</p>
  <div class="feedback-input abs">Enter your feedback</div>
  <div class="feedback-submit abs">Submit</div>
</section>

<footer class="site-footer abs">
  <h3 class="foot-head abs" style="left:118px;top:33px;font-weight:400">Quick links</h3>
  <div class="foot-rule abs" style="left:118px;top:62px;width:450px"></div>
  <nav class="quick-links abs">About<span>|</span>Terms of Use<span>|</span>Privacy<span>|</span>Cookies<span>|</span>FAQs<span>|</span>Contacts<span>|</span>Links<span>|</span>Affiliates</nav>
  <h3 class="foot-head abs" style="left:842px;top:33px;font-weight:400">Follow us on</h3>
  <div class="foot-rule abs" style="left:842px;top:64px;width:144px"></div>
  <div class="social abs" style="left:842px"></div>
  <div class="social abs" style="left:867px"></div>
  <div class="social abs" style="left:892px"></div>
  <div class="social abs" style="left:917px"></div>
  <div class="social abs" style="left:942px"></div>
</footer>
<div class="copyright-bar abs">© 2014. All Rights Reserved</div>

</body>
</html>
```